8x8 Social Media Ad - Harbor Summit Expo

Attention Real Estate Agents
Please join us for our
Quarterly Real Estate Training Expo
The 2nd Saturday of February, May, August and November
Our Next Training Expo is _________________________________
From 9 am to 1 pm
at
Marlowe Suites Fernridge Station
4187 Copperleaf Lane, Greenbelt, MD 20770
Scheduled Speakers
9:00 am - Desmond Pryce - Orientation
9:30 am - Terrell Oakes - Multiple Income Streams / Keystone Track
10:00 am - Lorna Beckett - Marketing though Social Media
10:45 am - Raul Denning - Generating Business through Kelp-Nest
11:30 am - Tunde Adesemi - Real Estate Investing
12:15 pm - Marcus Oyelowo - (Main Speaker) Training Topic TBA
For more information call Desmond Pryce at (240) 555-0192 or email dpryce@harborsummithomes.example

```html
<!DOCTYPE html>
<html lang="en">
<head>
<meta charset="utf-8">
<title>Harbor Summit Expo – Quarterly Real Estate Training Expo</title>
<link rel="stylesheet" href="https://fonts.googleapis.com/css2?family=Bebas+Neue&family=Barlow+Condensed:wght@500;600&family=Montserrat:wght@400;700;800&display=swap">
<style>
  :root {
    --teal: #0b8a96;
    --teal-light: #2aa5ae;
    --navy: #1c2a45;
    --white: #ffffff;
  }
  html, body { margin: 0; padding: 0; overflow: hidden; background: var(--white); }
  .ad {
    position: relative; width: 1200px; height: 1200px; overflow: hidden;
    background: var(--white); font-family: "Montserrat", sans-serif; color: var(--navy);
  }
  .ad-shapes { position: absolute; inset: 0; }
  .brand {
    position: absolute; left: 92px; top: 34px; display: flex; align-items: center; gap: 12px;
    font-family: "Bebas Neue", sans-serif; font-size: 44px; line-height: 1; color: var(--teal);
    letter-spacing: 1px; white-space: nowrap; z-index: 2;
  }
  .brand-mark { width: 24px; height: 24px; background: var(--teal); }
  .headline {
    position: absolute; left: 30px; top: 136px; margin: 0;
    font-family: "Bebas Neue", sans-serif; font-weight: 400; font-size: 137px;
    line-height: 0.77; color: var(--teal); letter-spacing: -1px; white-space: nowrap;
  }
  .invite {
    position: absolute; left: 31px; top: 378px; margin: 0;
    font-weight: 800; font-size: 35px; line-height: 51px; text-transform: uppercase;
  }
  .accent { color: var(--teal); }
  .schedule-note {
    position: absolute; left: 31px; top: 555px; margin: 0;
    font-family: "Barlow Condensed", sans-serif; font-weight: 600; font-size: 29px;
    line-height: 29px; color: var(--teal); text-transform: uppercase;
  }
  .date-line {
    position: absolute; left: 31px; top: 664px; width: 282px;
    border-top: 2px dashed var(--teal);
  }
  .hours {
    position: absolute; left: 31px; top: 700px; margin: 0;
    font-family: "Barlow Condensed", sans-serif; font-weight: 600; font-size: 29px;
    color: var(--teal); text-transform: uppercase;
  }
  .speakers-title {
    position: absolute; left: 38px; top: 770px; margin: 0;
    font-weight: 700; font-size: 21px; text-transform: uppercase;
  }
  .speakers {
    position: absolute; left: 32px; top: 806px; width: 640px; margin: 0; padding-left: 24px;
    font-size: 19.6px; line-height: 26.7px; color: var(--navy);
  }
  .speakers .nowrap { white-space: nowrap; }
  .venue {
    position: absolute; left: 68px; top: 1031px; margin: 0;
    font-weight: 700; font-size: 16.5px; line-height: 23px; color: var(--teal);
  }
  .venue-pin { position: absolute; left: 23px; top: 1031px; }
  .contact {
    position: absolute; left: 34px; top: 1128px; display: flex; align-items: center;
    font-size: 19px; color: var(--teal); white-space: nowrap;
  }
  .contact-label { font-weight: 700; color: var(--navy); margin-right: 28px; text-transform: uppercase; }
  .contact-item { display: flex; align-items: center; gap: 6px; margin-right: 26px; }
</style>
</head>
<body>
<main class="ad">
  <svg class="ad-shapes" width="1200" height="1200" viewBox="0 0 1200 1200">
    <defs>
      <linearGradient id="photoTones" x1="0" y1="0" x2="0" y2="1">
        <stop offset="0" stop-color="#e9eef1"/>
        <stop offset="0.35" stop-color="#b9c0c6"/>
        <stop offset="0.62" stop-color="#d8dadb"/>
        <stop offset="0.78" stop-color="#86a85a"/>
        <stop offset="1" stop-color="#5f8a2f"/>
      </linearGradient>
      <linearGradient id="portraitTones" x1="0" y1="0" x2="1" y2="1">
        <stop offset="0" stop-color="#3d3a3a"/>
        <stop offset="1" stop-color="#1e2430"/>
      </linearGradient>
    </defs>
    <polygon class="corner-accent" points="0,0 82,0 0,160" fill="var(--teal)"/>
    <polygon class="corner-accent" points="372,0 452,0 398,92" fill="var(--teal)"/>
    <g role="img" aria-label="Photo of a grey shingled house with a white wraparound porch and green lawn">
      <polygon points="778,52 1200,52 1200,950 817,950 522,500" fill="url(#photoTones)"/>
    </g>
    <polyline points="1200,50 778,50 520,500 815,952 1200,952" fill="none" stroke="var(--teal)" stroke-width="5"/>
    <g role="img" aria-label="Portrait of speaker Terrell Oakes in a blue suit">
      <polygon points="548,558 594,478 686,478 732,558 686,638 594,638" fill="url(#portraitTones)"/>
    </g>
    <g role="img" aria-label="Portrait of two speakers seated together">
      <polygon points="561,728 606,648 696,648 740,728 696,808 606,808" fill="#2a2e35"/>
    </g>
    <g role="img" aria-label="Portrait of speaker Lorna Beckett">
      <polygon points="690,855 737,775 833,775 880,855 833,935 737,935" fill="#d9d6d2" stroke="var(--white)" stroke-width="3"/>
    </g>
    <g role="img" aria-label="Portrait of speaker Tunde Adesemi outdoors">
      <polygon points="857,942 905,860 1000,860 1048,942 1000,1025 905,1025" fill="#7f8f6e" stroke="var(--white)" stroke-width="3"/>
    </g>
    <g role="img" aria-label="Portrait of main speaker Marcus Oyelowo in a hat">
      <polygon points="1045,933 1083,855 1162,855 1200,933 1162,1012 1083,1012" fill="#c9cccf" stroke="var(--white)" stroke-width="3"/>
    </g>
    <rect class="footer-band" x="0" y="1167" width="1200" height="33" fill="var(--teal)"/>
  </svg>

  <div class="brand"><span class="brand-mark"></span>Harbor Summit</div>

  <h1 class="headline">Attention<br>Real Estate Agents</h1>

  <p class="invite">Please <span class="accent">join us</span> for our<br>quarterly real estate<br><span class="accent">training expo</span></p>

  <p class="schedule-note">The 2nd Saturday of February, May, August<br>and November<br>Our next training expo is</p>
  <div class="date-line"></div>
  <p class="hours">From 9 am to 1 pm</p>

  <h2 class="speakers-title">Scheduled Speakers</h2>
  <ul class="speakers">
    <li>9:00 am - Desmond Pryce - Orientation</li>
    <li>9:30 am - Terrell Oakes - Multiple Income Streams / Keystone Track</li>
    <li class="nowrap">10:00 am - Lorna Beckett - Marketing though Social Media</li>
    <li class="nowrap">10:45 am - Raul Denning - Generating Business through Kelp-Nest</li>
    <li class="nowrap">11:30 am - Tunde Adesemi - Real Estate Investing</li>
    <li class="nowrap">12:15 pm - Marcus Oyelowo - (Main Speaker) Training Topic TBA</li>
  </ul>

  <svg class="venue-pin" width="32" height="46" viewBox="0 0 32 46" aria-hidden="true">
    <path d="M16 0C7 0 0 7 0 16c0 12 16 30 16 30s16-18 16-30C32 7 25 0 16 0z" fill="var(--navy)"/>
    <circle cx="16" cy="15" r="6" fill="var(--white)"/>
  </svg>
  <p class="venue">Marlowe Suites Fernridge Station<br>4187 Copperleaf Lane, Greenbelt, MD 20770</p>

  <div class="contact">
    <span class="contact-label">More Information</span>
    <span class="contact-item">
      <svg width="22" height="22" viewBox="0 0 24 24" aria-hidden="true"><path d="M6.6 10.8c1.4 2.8 3.8 5.1 6.6 6.6l2.2-2.2c.3-.3.7-.4 1-.2 1.1.4 2.3.6 3.6.6.6 0 1 .4 1 1V20c0 .6-.4 1-1 1C10.6 21 3 13.4 3 4c0-.6.4-1 1-1h3.5c.6 0 1 .4 1 1 0 1.3.2 2.5.6 3.6.1.3 0 .7-.2 1z" fill="var(--navy)"/></svg>
      Desmond Pryce at (240) 555-0192
    </span>
    <span class="contact-item">
      <svg width="28" height="20" viewBox="0 0 28 20" aria-hidden="true"><rect width="28" height="20" fill="var(--navy)"/><polyline points="1,1 14,11 27,1" fill="none" stroke="var(--white)" stroke-width="2"/></svg>
      dpryce@harborsummithomes.example
    </span>
  </div>
</main>
</body>
</html>
```